Falcrest security business card

Looking for a business card for my security company

Target Market(s)

Security

Industry/Entity Type

Security

Contact Information for Business Card

Name - Gil Marston. Title - General manager - direct 314 862.4490 website www. falcrestsecurityservices.example email - gil@ falcrestsecurityservices.example

Requirements
Must have
• Logo attached

```html
<!DOCTYPE html>
<html lang="en">
<head>
<meta charset="utf-8">
<title>Falcrest Security – Business Card</title>
<link rel="stylesheet" href="https://fonts.googleapis.com/css2?family=Montserrat:wght@400;500;600;700&display=swap">
<style>
  :root {
    --page: #e9e4dc;
    --card: #221a17;
    --gold-dark: #b4860f;
    --gold-mid: #d2ad4a;
    --gold-light: #ecd99a;
    --title-gold: #e39a14;
    --ink-light: #ffffff;
    --icon-ink: #2b2420;
  }
  * { box-sizing: border-box; margin: 0; padding: 0; }
  html, body {
    width: 1200px; height: 1200px; overflow: hidden;
    background: var(--page);
    font-family: "Montserrat", sans-serif;
  }
  .sheet {
    position: relative; width: 1200px; height: 1200px;
    display: flex; flex-direction: column; align-items: center;
    justify-content: center; gap: 52px;
  }
  .card {
    position: relative; width: 900px; height: 514px;
    background: var(--card); overflow: hidden;
    box-shadow: 0 6px 18px rgba(0,0,0,0.25);
  }
  .brand-word {
    font-family: "Montserrat", sans-serif; font-weight: 700;
    color: var(--gold-mid); letter-spacing: 2px; line-height: 1;
  }
  /* front */
  .card-front .brand-word {
    position: absolute; left: 0; width: 372px; top: 236px;
    text-align: center; font-size: 48px;
  }
  .gold-band {
    position: absolute; top: 0; bottom: 0; left: 372px; width: 80px;
    background: linear-gradient(180deg, var(--gold-dark) 0%, var(--gold-light) 48%, var(--gold-dark) 100%);
  }
  .person { position: absolute; left: 476px; top: 120px; }
  .person-name {
    color: var(--ink-light); font-weight: 700; font-size: 36px; letter-spacing: 3px;
  }
  .person-title {
    color: var(--title-gold); font-weight: 600; font-size: 25px; letter-spacing: 2.5px; margin-top: 4px;
  }
  .contacts { position: absolute; left: 414px; top: 300px; right: 48px; list-style: none; }
  .contacts li {
    display: flex; align-items: center; height: 60px;
    color: var(--ink-light); font-size: 18px; font-weight: 400; white-space: nowrap;
  }
  .contact-icon {
    width: 50px; height: 50px; border-radius: 50%; background: #fff;
    display: flex; align-items: center; justify-content: center;
    margin-right: 22px; flex: none;
  }
  .contact-icon svg { width: 26px; height: 26px; }
  /* back */
  .card-back { display: flex; align-items: center; justify-content: center; }
  .card-back .brand-word { font-size: 112px; letter-spacing: 6px; }
</style>
</head>
<body>
<main class="sheet">
  <section class="card card-front" aria-label="Business card front">
    <div class="brand-word">FALCREST</div>
    <div class="gold-band"></div>
    <div class="person">
      <div class="person-name">GIL MARSTON</div>
      <div class="person-title">General manager</div>
    </div>
    <ul class="contacts">
      <li>
        <span class="contact-icon">
          <svg viewBox="0 0 24 24" aria-hidden="true"><path fill="var(--icon-ink)" d="M6.6 10.8c1.4 2.8 3.8 5.1 6.6 6.6l2.2-2.2c.3-.3.7-.4 1-.2 1.1.4 2.3.6 3.6.6.6 0 1 .4 1 1V20c0 .6-.4 1-1 1C10.6 21 3 13.4 3 4c0-.6.4-1 1-1h3.5c.6 0 1 .4 1 1 0 1.3.2 2.5.6 3.6.1.3 0 .7-.2 1l-2.3 2.2z"/></svg>
        </span>
        314 862.4490
      </li>
      <li>
        <span class="contact-icon">
          <svg viewBox="0 0 24 24" aria-hidden="true" fill="none" stroke="var(--icon-ink)" stroke-width="1.4"><rect x="2.5" y="5.5" width="19" height="13"/><path d="M2.5 5.5l9.5 8 9.5-8M2.5 18.5l7-6.5M21.5 18.5l-7-6.5"/></svg>
        </span>
        gil@ falcrestsecurityservices.example
      </li>
      <li>
        <span class="contact-icon">
          <svg viewBox="0 0 24 24" aria-hidden="true" fill="none" stroke="var(--icon-ink)" stroke-width="1.2"><circle cx="12" cy="12" r="9.5"/><ellipse cx="12" cy="12" rx="4.5" ry="9.5"/><path d="M2.5 12h19M4 7h16M4 17h16M12 2.5v19"/></svg>
        </span>
        www. falcrestsecurityservices.example
      </li>
    </ul>
  </section>
  <section class="card card-back" aria-label="Business card back">
    <div class="brand-word">FALCREST</div>
  </section>
</main>
</body>
</html>
```